Tender Horizon yoga, meditation & wellness

I teach kundalini yoga and meditation classes.
I have adult beginner classes, seniors classes, family yoga classes, kids yoga classes
I also offer events like cacao ceremony, full moon ceremony, and retreats

Professional, and simple website that is easy to navigate, and easy for me to update, change.

Target Market(s)

all ages

Industry/Entity Type

Health And Wellness

Coding

Coded - Design and coding required

Number of Pages Required

5+ page

Font styles to use
Decorative

Colors
cedeed
eedded
e4daeb
fbd4d5
fee3d4

Requirements
Must have
• tabs required: about, contact, events, classes, blog,
• I would like to link my facebook page & instagram accounts to the website
Nice to have
• I would like my clients to be able to register for classes and events from my website
• I would like to have a "shop" option in the future, for some items that I have for sale

```html
<!DOCTYPE html>
<html lang="en">
<head>
<meta charset="utf-8">
<title>Tender Horizon — Yoga, Meditation &amp; Wellness</title>
<link href="https://fonts.googleapis.com/css2?family=Barlow:wght@300;400;500;600;700&display=swap" rel="stylesheet">
<style>
:root{
  --peach:#fee3d4;
  --blue:#cddcec;
  --pink:#fbd4d5;
  --lilac:#e4daeb;
  --accent:#8aa6c8;
  --accent-dark:#6f8fb8;
  --ink:#2b2b2b;
  --footer:#2a2627;
  --white:#ffffff;
  --placeholder:#dcdedd;
  --hero-blue:#e3eef7;
  --hero-pink:#f6e4f1;
}
*{box-sizing:border-box;margin:0;padding:0}
html,body{width:1200px;height:3333px;overflow:hidden}
body{position:relative;background:var(--white);font-family:"Barlow",sans-serif;color:var(--ink)}
.abs{position:absolute}
a{color:inherit;text-decoration:none}

/* top bar */
.topbar{left:0;top:0;width:1200px;height:73px;background:var(--peach);border-bottom:3px solid #d9e4f0}
.topbar .contact{right:52px;top:22px;font-size:22px;color:#444}

/* header */
.brand{left:52px;top:92px;display:flex;align-items:center;gap:18px}
.brand .dot{width:92px;height:92px;border-radius:50%;background:var(--pink)}
.brand .name{font-size:40px;font-weight:600;color:var(--accent);line-height:1;letter-spacing:1px}
.brand .tag{font-size:13px;font-weight:500;letter-spacing:1px;margin-top:8px;color:#333}
.nav{left:0;top:73px;width:1200px;height:140px}
.nav .rule{position:absolute;top:0;width:2px;height:95px;background:#d3e0ee}
.nav .item{position:absolute;top:84px;font-size:17px;letter-spacing:1.5px;color:#555}

/* hero */
.hero-bg{left:0;top:222px;width:1200px;height:711px;background:linear-gradient(180deg,var(--white) 0%,var(--hero-blue) 45%,var(--hero-pink) 70%,var(--white) 100%)}
.hero-title{right:638px;top:364px;text-align:right}
.hero-title h1{font-weight:300;font-size:60px;color:var(--accent);letter-spacing:2px;line-height:1}
.hero-title h2{font-weight:600;font-size:38px;color:#9a9a9a;letter-spacing:20px;margin-right:-20px;margin-top:6px;line-height:1}
.hero-title p{font-size:13px;color:#a0a0a0;width:300px;margin-left:auto;line-height:1.35;margin-top:14px}
.more{font-size:17px;font-weight:700;color:var(--accent-dark);letter-spacing:1px}
.hero-title .more{display:block;margin-top:12px}
.hero-photo{left:640px;top:365px;width:342px;height:432px;border-radius:40% 40% 30% 30%;background:linear-gradient(180deg,#e7e8ee,#cfd0d8 60%,#e9e6ee)}

/* nature */
.nature{left:0;top:965px;width:1200px;text-align:center}
.nature h2{font-weight:300;font-size:54px;color:var(--accent)}
.nature p{font-size:15px;color:#a3a3a3;width:640px;margin:6px auto 0;line-height:1.45}

/* cards */
.card{top:1162px;width:307px;height:420px;border-radius:12px}
.card h3{text-align:center;font-weight:400;font-size:28px;color:var(--accent);letter-spacing:1px;margin-top:30px}
.card .divider{height:2px;width:254px;margin:14px auto 0;background:linear-gradient(90deg,transparent,#fff,transparent)}
.card-classes{left:111px;background:var(--blue)}
.card-events{left:451px;background:var(--pink)}
.card-shop{left:784px;background:var(--lilac)}
.class-list{list-style:none;margin:24px 0 0 28px}
.class-list li{font-size:22px;color:#333;height:45px;display:flex;align-items:center;gap:18px}
.class-list li::before{content:"";width:12px;height:12px;border-radius:50%;background:#333}
.event-photo{position:absolute;left:29px;top:109px;width:255px;height:129px;border-radius:14px;background:linear-gradient(180deg,#7e8f5e,#c7b8a6 55%,#9aa077)}
.card-text{position:absolute;font-size:15.5px;line-height:1.35;color:#444;text-align:justify}
.card-events .date{position:absolute;left:31px;top:262px;font-size:15.5px;font-weight:600;color:#333}
.card-events .card-text{left:31px;top:282px;width:250px}
.shop-photo{position:absolute;left:94px;top:105px;width:100px;height:182px;border-radius:8px;background:linear-gradient(180deg,#c9b7b3,#ad9c99)}
.card-shop .card-text{left:30px;top:306px;width:250px}

/* about */
.about-photo{left:135px;top:1749px;width:236px;height:236px;border-radius:50%;background:linear-gradient(135deg,#33453b,#c98d6d 55%,#ede5df)}
.about{left:440px;top:1705px;width:654px;text-align:center}
.about h2{font-weight:300;font-size:54px;color:var(--accent)}
.about .person{font-size:22px;color:var(--accent);margin-top:8px}
.about p{font-size:17px;line-height:1.35;color:#333;margin-top:14px}
.about .more{display:block;margin-top:22px}
.book{left:308px;top:2050px;font-size:28px;color:var(--accent)}
.book b{font-weight:700}

/* blog band */
.band{left:0;top:2133px;width:1200px;height:511px;background:var(--peach)}
.band-art{left:111px;top:2229px;width:320px;height:320px;border-radius:50%;background:radial-gradient(circle,#3f3a3a 0 22%,#d9cfb5 40%,#b9c7b3 62%,#f7ecdf 72%)}
.band-text{left:465px;top:2200px;width:604px;text-align:center}
.band-text h2{font-weight:400;font-size:60px;color:#111;line-height:1}
.band-text p{font-size:17px;line-height:1.35;color:#333;margin-top:22px}
.band-text h3{font-size:24px;font-weight:700;margin-top:50px;color:#111}
.band-text h3 + p{margin-top:8px}
.btn{left:616px;top:2538px;width:304px;height:58px;border-radius:14px;background:var(--white);font-size:30px;display:flex;align-items:center;justify-content:center;color:#222;letter-spacing:1px}

/* testimonies */
.testimonies-title{left:118px;top:2680px;font-size:54px;font-weight:400;color:#111}
.avatar{width:106px;height:106px;border-radius:50%;background:var(--placeholder)}
.quote{font-size:17px;line-height:1.3;color:#333;width:330px}
.testi-more{right:80px;top:2896px}

/* footer */
.footer{left:0;top:2964px;width:1200px;height:296px;background:var(--footer)}
.foot-brand{left:89px;top:3018px;display:flex;align-items:center;gap:14px}
.foot-brand .dot{width:78px;height:78px;border-radius:50%;background:var(--pink)}
.foot-brand .name{font-size:34px;font-weight:600;color:#c8d5e6;line-height:1}
.foot-brand .tag{font-size:11px;color:#eee;letter-spacing:1px;margin-top:6px}
.foot-contact{left:100px;top:3138px;color:#a9c4e6}
.foot-contact .phone{font-size:28px;font-weight:300}
.foot-contact .email{font-size:19px;margin-top:2px}
.foot-head{font-size:32px;font-weight:300;color:#6b6b6b;letter-spacing:1px}
.links{list-style:none;font-size:14px;color:#eee;font-weight:500}
.links li{height:29px;display:flex;align-items:center;gap:10px}
.links li::before{content:"";width:7px;height:7px;border-radius:50%;background:#eee}
.read-all{left:487px;top:3192px;font-size:13px;color:#9ab9e6}
.social{left:904px;top:3066px;display:flex;gap:4px}
.social span{width:38px;height:38px;border-radius:50%;background:#3d8fd6}

/* copyright */
.copyright{left:0;top:3260px;width:1200px;height:73px;background:var(--peach);font-size:16px;color:#222;padding:28px 0 0 84px;letter-spacing:.3px}
</style>
</head>
<body>

<div class="abs topbar"><div class="abs contact">204-555-0182 &nbsp;|&nbsp; Register Now</div></div>

<div class="abs hero-bg" role="img" aria-label="Soft pastel light-wave background artwork"></div>

<div class="abs nav">
  <span class="rule" style="left:596px"></span><span class="rule" style="left:733px"></span><span class="rule" style="left:840px"></span><span class="rule" style="left:944px"></span><span class="rule" style="left:1036px"></span>
  <a class="item" style="left:518px">HOME</a>
  <a class="item" style="left:613px">ABOUT US</a>
  <a class="item" style="left:744px">CLASSES</a>
  <a class="item" style="left:866px">EVENT</a>
  <a class="item" style="left:966px">SHOP</a>
  <a class="item" style="left:1060px">CONTACT US</a>
</div>

<div class="abs brand">
  <span class="dot"></span>
  <div><div class="name">TENDER HORIZON</div><div class="tag">YOGA, MEDITATION &amp; WELLNESS</div></div>
</div>

<div class="abs hero-title">
  <h1>KUNDALINI</h1>
  <h2>YOGA</h2>
  <p>Kundalini Yoga comes from northern India and has a centuries-long tradition. It was brought to the West by Yogi Devan in 1968.</p>
  <a class="more">VIEW MORE</a>
</div>
<div class="abs hero-photo" role="img" aria-label="Photo of the teacher seated cross-legged in meditation"></div>

<section class="abs nature">
  <h2>Nature of Yoga</h2>
  <p>Kundalini Yoga comes from northern India and has a centuries-long tradition. It was brought to the West by Yogi Devan in 1968.</p>
</section>

<section class="abs card card-classes">
  <h3>CLASSES</h3><div class="divider"></div>
  <ul class="class-list">
    <li>Yogi Devan</li><li>Sat Nam Rasayan</li><li>Ayurveda</li><li>Numerology</li><li>Tantric Yoga</li><li>Gatka</li>
  </ul>
</section>
<section class="abs card card-events">
  <h3>EVENTS</h3><div class="divider"></div>
  <div class="event-photo" role="img" aria-label="Photo of children in white dresses with flower crowns outdoors"></div>
  <div class="date">12-10-2018</div>
  <p class="card-text">Wear loose fitted clothing that is comfortable moves with you. You may wish to wear layers as your body temperature will likely change during practice,</p>
</section>
<section class="abs card card-shop">
  <h3>SHOP</h3><div class="divider"></div>
  <div class="shop-photo" role="img" aria-label="Photo of a printed canvas tote bag"></div>
  <p class="card-text">Wear loose fitted clothing that is comfortable moves with you. You may wish to</p>
</section>

<div class="abs about-photo" role="img" aria-label="Portrait photo of the teacher"></div>
<section class="abs about">
  <h2>About Us</h2>
  <div class="person">Maren (Sat Anand Kaur)</div>
  <p>I have been practicing yoga for about 5 years, I began practicing Kundalini yoga 2 years ago, and it ignited a complete transformation of mind, body and spirit. I knew that I would go on to teach this lineage.</p>
  <p style="margin-top:26px">I’m also a nurse part time with the NRHC, my 18 years of health care experience has been invaluable. My most important job of all is wife, mother and home educator to my four daughters, ages 9-4 years.</p>
  <a class="more">VIEW MORE</a>
</section>
<div class="abs book"><b>Book Now</b> : - 204-555-0182 &nbsp;|&nbsp; tenderhorizonyoga@example.com</div>

<div class="abs band"></div>
<div class="abs band-art" role="img" aria-label="Illustration of a meditating figure framed by a lettered mandala wreath"></div>
<section class="abs band-text">
  <h2>what’s right for you.</h2>
  <p>I have been practicing yoga for about 5 years, I began practicing Kundalini yoga 2 years ago, and it ignited a complete transformation of mind, body and spirit. I knew that I would go on to teach this lineage.</p>
  <h3>What Can Expect in a Typical Class?</h3>
  <p>I have been practicing yoga for about 5 years, I began practicing Kundalini yoga 2 years ago, and it ignited a complete transformation of mind, body and spirit. I knew that I would go on to teach this lineage.</p>
</section>
<a class="abs btn">VIEW MORE BLOGS</a>

<h2 class="abs testimonies-title">Testimonies</h2>
<div class="abs avatar" style="left:100px;top:2769px" role="img" aria-label="Client photo"></div>
<p class="abs quote" style="left:229px;top:2776px">I have been practicing yoga for about 5 years, I began practicing Kundalini yoga 2 years ago, and it ignited a complete transformation of mind,</p>
<div class="abs avatar" style="left:585px;top:2769px" role="img" aria-label="Client photo"></div>
<p class="abs quote" style="left:713px;top:2776px">I have been practicing yoga for about 5 years, I began practicing Kundalini yoga 2 years ago, and it ignited a complete transformation of mind,</p>
<a class="abs more testi-more">VIEW MORE</a>

<footer class="abs footer"></footer>
<div class="abs foot-brand">
  <span class="dot"></span>
  <div><div class="name">TENDER HORIZON</div><div class="tag">YOGA, MEDITATION &amp; WELLNESS</div></div>
</div>
<div class="abs foot-contact"><div class="phone">204-555-0182</div><div class="email">tenderhorizonyoga@example.com</div></div>
<div class="abs foot-head" style="left:484px;top:3006px">QUICK LINKS</div>
<ul class="abs links" style="left:493px;top:3060px"><li>ABOUT US</li><li>CLASSES</li><li>EVENT</li><li>SHOP</li></ul>
<ul class="abs links" style="left:678px;top:3060px"><li>BLOG</li><li>TESTIMONIALS</li><li>REGISTER</li><li>CONTACT US</li></ul>
<a class="abs read-all">Read All</a>
<div class="abs foot-head" style="left:904px;top:3006px">FOLLOW US</div>
<div class="abs social" role="img" aria-label="Social media links">
  <span></span><span></span><span></span><span></span><span></span><span></span>
</div>

<div class="abs copyright">COPYRIGHT 2018 © TENDER HORIZON. &nbsp;ALL RIGHTS RESERVED</div>

</body>
</html>
```